Coffee Promotion for Specialty Coffees

I need to have a poster designed to promote our coffee sales. We offer cappuccino for $3.75, Latte for $3.75, Americano for $2.00, Espresso $2.00 and Fair Trade Organic Colombian Coffee for $1.75 Med, $2.00L Large. I would like sometihng very visual that shows the coffees and also has the pricing, and includes the wording" Try our Amazing Specialty Coffees!" Our logo is attached as well

Poster size is 24" wide x 36" high

Target Market(s)

Seniors and Students in a Mall Setting

Colors

Designer to choose colors to be used in the design.

Requirements
Must have
• Graphic artwork of coffees (cappuccinos, lattes, etc). Logo included in artwork. Must be for 24"wide x 36" high poster
Nice to have
• Would like something that shows closeups of the coffees and visually sells the coffee being premium and delicious.

```html
<!DOCTYPE html>
<html lang="en">
<head>
<meta charset="utf-8">
<title>Specialty Coffees Poster</title>
<link href="https://fonts.googleapis.com/css2?family=Bebas+Neue&family=Montserrat:wght@700;800&display=swap" rel="stylesheet">
<style>
  :root {
    --ink: #050505;
    --white: #ffffff;
    --orange: #ec6420;
    --rule-grey: #8a8a8a;
    --photo-light: #a9a9a9;
    --photo-mid: #5e5e5e;
    --photo-dark: #1e1e1e;
  }
  html, body {
    margin: 0;
    padding: 0;
    width: 802px;
    height: 1200px;
    overflow: hidden;
    background: var(--ink);
  }
  .poster {
    position: relative;
    width: 802px;
    height: 1200px;
    background: var(--ink);
    overflow: hidden;
    font-family: "Montserrat", sans-serif;
    color: var(--white);
  }
  .coffee-photo {
    position: absolute;
    left: 0;
    top: 440px;
    width: 802px;
    height: 760px;
    background:
      radial-gradient(ellipse 230px 150px at 420px 420px, #d8d8d8 0%, #9c9c9c 45%, transparent 75%),
      radial-gradient(ellipse 320px 240px at 430px 560px, var(--photo-mid) 0%, transparent 80%),
      linear-gradient(160deg, var(--photo-dark) 0%, var(--photo-mid) 45%, var(--photo-light) 75%, var(--photo-mid) 100%);
  }
  .coffee-photo::before {
    content: "";
    position: absolute;
    inset: 0;
    background: linear-gradient(180deg, var(--ink) 0%, rgba(5,5,5,0.85) 20%, rgba(5,5,5,0) 55%);
  }
  .brand {
    position: absolute;
    left: 0;
    top: 90px;
    width: 802px;
    text-align: center;
    font-family: "Montserrat", sans-serif;
    font-weight: 700;
    font-size: 30px;
    line-height: 40px;
    color: var(--white);
  }
  .headline-kicker {
    position: absolute;
    top: 226px;
    left: 0;
    width: 802px;
    display: flex;
    align-items: center;
    justify-content: center;
    gap: 10px;
    font-family: "Bebas Neue", sans-serif;
    font-size: 46px;
    line-height: 1;
  }
  .headline-kicker .rule {
    width: 142px;
    height: 3px;
    background: var(--orange);
  }
  .headline {
    position: absolute;
    top: 276px;
    left: 0;
    width: 802px;
    margin: 0;
    text-align: center;
    font-family: "Bebas Neue", sans-serif;
    font-weight: 400;
    font-size: 92px;
    line-height: 1;
    letter-spacing: 1px;
  }
  .accent { color: var(--orange); }
  .offer-title {
    position: absolute;
    top: 390px;
    left: 0;
    width: 802px;
    display: flex;
    align-items: center;
    justify-content: center;
    gap: 14px;
    font-family: "Bebas Neue", sans-serif;
    font-size: 60px;
    line-height: 1;
    color: var(--orange);
  }
  .offer-title .rule {
    flex: 1;
    height: 2px;
    background: var(--rule-grey);
  }
  .menu {
    position: absolute;
    top: 455px;
    left: 18px;
    width: 766px;
    display: flex;
    justify-content: center;
    font-weight: 800;
    font-size: 25px;
    line-height: 42px;
  }
  .menu-col {
    list-style: none;
    margin: 0;
    padding: 0 14px;
  }
  .menu-col + .menu-col { border-left: 2px solid var(--white); }
  .menu-col li::before {
    content: "•";
    color: var(--orange);
    margin-right: 9px;
  }
  .price { color: var(--orange); }
  .featured-box {
    position: absolute;
    top: 554px;
    left: 111px;
    width: 578px;
    height: 88px;
    box-sizing: border-box;
    border: 2px dashed #bdbdbd;
    text-align: center;
    font-weight: 800;
    font-size: 25px;
    line-height: 34px;
    padding-top: 9px;
  }
  .large-price {
    position: absolute;
    top: 656px;
    left: 0;
    width: 802px;
    text-align: center;
    font-family: "Bebas Neue", sans-serif;
    font-size: 78px;
    line-height: 1;
  }
</style>
</head>
<body>
  <main class="poster">
    <div class="coffee-photo" role="img" aria-label="Black and white close-up of a cappuccino with leaf latte art in a white cup on a wooden tray with a spoon"></div>

    <div class="brand">Maple Row Café</div>

    <div class="headline-kicker"><span class="rule"></span>Try Our Amazing<span class="rule"></span></div>
    <h1 class="headline">Specialty <span class="accent">Coffees</span></h1>

    <div class="offer-title"><span class="rule"></span>We Offer<span class="rule"></span></div>

    <div class="menu">
      <ul class="menu-col">
        <li>CAPPUCCINO FOR -<span class="price">$3.75</span></li>
        <li>LATTE FOR -<span class="price">$3.75</span></li>
      </ul>
      <ul class="menu-col">
        <li>AMERICANO FOR -<span class="price">$2.00</span></li>
        <li>ESPRESSO -<span class="price">$2.00</span></li>
      </ul>
    </div>

    <div class="featured-box">
      FAIR TRADE ORGANIC<br>
      COLOMBIAN COFFEE OR <span class="price">$1.75</span> MED
    </div>

    <div class="large-price"><span class="accent">$2.00-</span>Large</div>
  </main>
</body>
</html>
```